Geschäftspapiere für Hundebetreuung
Zielgruppe
Mein Unternehmen richtet sich an Hundehalter, die freudig mit ihrem Hund arbeiten oder trainieren wollen oder eine positiv arbeitende Hundebetreuung oder Gassi-Gänger suchen. Hierbei liegt der Fokus auf Emotionen des Hundes, Emotionen des Hundehalters, Körpersprache und kleinschrittiges Training. Gemeinsames freudiges Training schafft Vertrauen und Bindung und ermöglicht Hund und Halter Freiraum. Ziel des Angebotes ist es, dass Hundehalter Verständnis für die Emotionen und Interessen des Hundes zu entwickeln und das für sich zu nutzen lernen, dem Hund das geben, was er in der jeweiligen Situation braucht und das ganze auf wissenschaftlich fundierter Basis.
Aufgabenstellung
Das Logo muss enthalten sein, ansonsten sind der Kreativität keine Grenzen gesetzt :)
Es sollte nur von Rechnung, über Angebot für alles nutzbar sein.
Das Unternehmen ist ein Einzelunternehmen, sprich der Firmenname ist mein eigener Name 'Sabine Krollmann' und Pfotenfreunde nur Website und Marke.

```html
<!DOCTYPE html>
<html lang="de">
<head>
<meta charset="utf-8">
<title>Pfotenfreunde – Briefbogen</title>
<link href="https://fonts.googleapis.com/css2?family=Delius&display=swap" rel="stylesheet">
<style>
  :root {
    --backdrop: #b5bab7;
    --paper: #ffffff;
    --ink: #1e1e1e;
    --brand-green: #8bb833;
    --brand-dark: #3d4f55;
    --mark: #3a3a3a;
  }
  * { margin: 0; padding: 0; box-sizing: border-box; }
  html, body { width: 895px; height: 1200px; overflow: hidden; }
  body {
    background: var(--backdrop);
    font-family: "Delius", cursive;
    color: var(--ink);
    position: relative;
  }
  .letterhead {
    position: absolute;
    left: 62px; top: 55px;
    width: 770px; height: 1089px;
    background: var(--paper);
  }
  .brand {
    position: absolute;
    left: 524px; top: 150px;
    width: 207px;
    display: flex; align-items: center; gap: 8px;
    justify-content: center;
  }
  .brand-dot {
    width: 14px; height: 14px; border-radius: 50%;
    background: var(--brand-green);
  }
  .brand-name {
    font-size: 30px;
    color: var(--brand-green);
    line-height: 1;
  }
  .sender-line {
    position: absolute;
    left: 96px; top: 213px;
    font-size: 8.5px;
  }
  .fold-mark {
    position: absolute; left: 0;
    width: 19px; height: 1px;
    background: var(--mark);
  }
  .fold-mark.upper { top: 384px; }
  .fold-mark.lower { top: 769px; }
  .contact-block {
    position: absolute;
    left: 563px; top: 204px;
    font-size: 10.5px;
    line-height: 14px;
  }
  .contact-name {
    font-size: 19px;
    color: var(--brand-green);
    line-height: 24px;
    margin-bottom: 1px;
  }
  .contact-list {
    list-style: none;
    margin-top: 15px;
  }
  .contact-list li {
    display: flex; align-items: center; gap: 8px;
    height: 15.8px;
  }
  .contact-list svg {
    width: 10px; height: 10px;
    fill: none; stroke: var(--brand-green); stroke-width: 1.4;
    flex: none;
  }
  .footer {
    position: absolute;
    left: 78px; top: 1014px;
    font-size: 9.4px;
    line-height: 13.6px;
    white-space: nowrap;
  }
</style>
</head>
<body>
  <main class="letterhead">
    <div class="brand">
      <span class="brand-dot"></span>
      <span class="brand-name">Pfotenfreunde</span>
    </div>

    <p class="sender-line">Sabine Krollmann | Lindenweg 12 | 48151 Sandfeld</p>

    <span class="fold-mark upper"></span>
    <span class="fold-mark lower"></span>

    <address class="contact-block" style="font-style:normal">
      <p class="contact-name">Sabine Krollmann</p>
      <p>Lindenweg 12</p>
      <p>48151 Sandfeld</p>
      <ul class="contact-list">
        <li>
          <svg viewBox="0 0 10 10" aria-hidden="true"><path d="M2 1 L4 3 L3 4.2 Q4.5 6.5 6 7 L7 6 L9 8 L7.8 9.2 Q3 8.5 0.8 2.2 Z"/></svg>
          +49 (0)1234 5 67 89-0
        </li>
        <li>
          <svg viewBox="0 0 10 10" aria-hidden="true"><rect x="2.5" y="0.8" width="5" height="8.4" rx="1"/><line x1="4.2" y1="7.6" x2="5.8" y2="7.6"/></svg>
          +49 (0)1234 5 67 89-50
        </li>
        <li>
          <svg viewBox="0 0 10 10" aria-hidden="true"><rect x="0.8" y="3.5" width="8.4" height="4.5" rx="1"/><rect x="2.5" y="1" width="5" height="2.5"/><rect x="2.5" y="6" width="5" height="3"/></svg>
          +49 (0)123 4 56 78 90
        </li>
        <li>
          <svg viewBox="0 0 10 10" aria-hidden="true"><rect x="0.8" y="2" width="8.4" height="6"/><path d="M0.8 2 L5 5.5 L9.2 2"/></svg>
          info@yourcompany.de
        </li>
        <li>
          <svg viewBox="0 0 10 10" aria-hidden="true"><circle cx="5" cy="5" r="4.2"/><ellipse cx="5" cy="5" rx="1.8" ry="4.2"/><line x1="0.8" y1="5" x2="9.2" y2="5"/></svg>
          yourcompany.de
        </li>
      </ul>
    </address>

    <footer class="footer">
      <p>Max Mustermann | Geschäftsführer | Musterweg 13 | 54321 Musterdorf</p>
      <p>Telefon +49 (0)1234 5 67 89-0 | Telefax +49 (0)1234 5 67 89-50 | Mobil +49 (0)123 4 56 78 90 | info@yourcompany.de | yourcompany.de</p>
      <p>Nordbank IBAN DE00 1234 5678 9012 3456 78 | BIC NORDDEXX | Amtsgericht Musterstadt HRN 125915 Gerichtsstand Musterstadt</p>
    </footer>
  </main>
</body>
</html>
```